Brindlemoor Copper Works

I created the attached in quill mark. I would like the background to look like black leather and the text to be gold. Any other suggestions would be appreciated. Thank you
Please note: all text now should be white .... sorry Partners changed their mind
Please remember when submitting designs, this design is for a folded business card with printing on all 4 sides ..... thank you
Also, the front of the card must have the wording above the logo. These will be placed in the wallet ID pockets and I would like to be able to read the wording.
Printing
I would like a folded business card. I created one in Quillmark but don't know how to send it to you to apply the final touches.

```html
<!DOCTYPE html>
<html lang="en">
<head>
<meta charset="utf-8">
<title>Brindlemoor Copper Works – Folded Business Card</title>
<link rel="stylesheet" href="https://fonts.googleapis.com/css2?family=Cormorant+Garamond:ital,wght@1,500;1,600&family=Questrial&display=swap">
<style>
  :root {
    --page-bg: #d4d4d4;
    --leather-dark: #0b0b0b;
    --leather-mid: #2a2a2a;
    --inset-panel: rgba(90, 90, 90, 0.45);
    --ink: #ffffff;
    --ink-faint: rgba(0, 0, 0, 0.35);
    --script: "Cormorant Garamond", Georgia, serif;
    --sans: "Questrial", Arial, sans-serif;
  }
  * { box-sizing: border-box; margin: 0; padding: 0; }
  html, body { width: 1200px; height: 900px; overflow: hidden; }
  body { background: var(--page-bg); position: relative; color: var(--ink); }

  .card-face {
    position: absolute;
    top: 137px;
    height: 613px;
    background: radial-gradient(ellipse at 45% 45%, var(--leather-mid) 0%, #151515 55%, var(--leather-dark) 100%);
  }
  .card-face--outside { left: 52px; width: 531px; }
  .card-face--inside { left: 620px; width: 530px; }

  /* back panel, printed upside down for the fold */
  .contact-block {
    position: absolute;
    left: 0; right: 0; top: 168px;
    transform: rotate(180deg);
    text-align: center;
    font-family: var(--sans);
    line-height: 1.2;
  }
  .contact-block .brand-mark { margin-bottom: 18px; }
  .contact-block .names { font-size: 19px; margin-bottom: 4px; }
  .contact-block .detail { font-size: 14px; letter-spacing: 0.3px; }

  .brand-mark {
    display: inline-flex; align-items: center; gap: 8px;
    font-family: var(--script); font-style: italic; font-weight: 600;
    color: var(--ink);
  }
  .brand-mark .dot {
    width: 12px; height: 12px; border-radius: 50%; background: var(--ink);
  }
  .contact-block .brand-mark { font-size: 15px; }

  .front-tagline {
    position: absolute; left: 0; right: 0; top: 345px;
    text-align: center;
    font-family: var(--script); font-style: italic; font-weight: 500;
    font-size: 27px; letter-spacing: 0.8px;
  }
  .front-brand {
    position: absolute; left: 0; right: 0; top: 490px;
    text-align: center;
  }
  .front-brand .brand-mark { font-size: 26px; }
  .front-brand .dot { width: 18px; height: 18px; }

  .inset-panel {
    position: absolute; left: 31px; top: 33px; width: 467px; height: 546px;
    background: var(--inset-panel);
  }
  .inset-panel .faint-brand {
    position: absolute; left: 0; right: 0; top: 240px;
    text-align: center;
    font-family: var(--script); font-style: italic; font-weight: 600;
    font-size: 34px; color: var(--ink-faint);
  }
  .inside-copy {
    position: absolute; left: 19px; right: 19px; top: 38px;
    font-family: var(--script); font-style: italic; font-weight: 500;
    font-size: 18.5px; line-height: 23px; letter-spacing: 0.4px;
  }
  .inside-copy p { margin-bottom: 46px; }
  .inside-copy .welcome { text-align: center; }
  .inside-copy .justified { text-align: justify; text-align-last: center; }
</style>
</head>
<body>
  <section class="card-face card-face--outside" aria-label="Outside of folded card">
    <div class="contact-block">
      <div class="brand-mark"><span class="dot"></span>Brindlemoor Copper Works</div>
      <p class="names">Dorian &amp; Wren Halloway</p>
      <p class="detail">Phone: 0400 555 018</p>
      <p class="detail">PO BOX 412</p>
      <p class="detail">ELDERVALE, WESTERN AUSTRALIA, 6999</p>
    </div>
    <h1 class="front-tagline">100% Brindlemoor Copper Works</h1>
    <div class="front-brand">
      <div class="brand-mark"><span class="dot"></span>Brindlemoor Copper Works</div>
    </div>
  </section>

  <section class="card-face card-face--inside" aria-label="Inside of folded card">
    <div class="inset-panel">
      <div class="faint-brand" aria-hidden="true">Brindlemoor Copper Works</div>
      <div class="inside-copy">
        <p class="welcome">Congratulations, you have purchased an exquisite exclusive item from Brindlemoor Copper Works.</p>
        <p class="justified">Each item has been tailored to the last stitch, each piece is produced under the eye of our expert artisan. Using best tanning processes here in Australia our leather never loses its colour.</p>
        <p class="justified">Alpaca leather is a luxurious fine grained leather known for its beauty and wear resistance. Alpaca leather, though thinner and lighter weight than traditional hides has a much higher tensile strength which means it won’t stretch and sag. Alpaca items maintain their shape beautifully due to its inherent tensile strength and suppleness.</p>
      </div>
    </div>
  </section>
</body>
</html>
```